Motivating Modern Poster for Top Selling Reps

We need a poster design for our Sales reps at our Solar company. Our company's mission is to disrupt the energy monopoly and give our customers a choice in how they get their energy. Our sales reps need a street style, modern poster with this quote:
"Practice until you never get it wrong"
Here are a few examples of what has been done previously and our logo. The final design should motivate.

```html
<!DOCTYPE html>
<html lang="en">
<head>
<meta charset="utf-8">
<title>Practice Until You Never Get It Wrong — Sales Poster</title>
<link href="https://fonts.googleapis.com/css2?family=Black+Ops+One&display=swap" rel="stylesheet">
<style>
  :root {
    --backdrop: #e4e6e8;
    --poster-ink: #050505;
    --solar-blue: #149fd3;
    --chalk-white: #e9e9e9;
  }
  html, body {
    margin: 0;
    width: 1200px;
    height: 1200px;
    overflow: hidden;
    background: var(--backdrop);
  }
  .poster {
    position: absolute;
    left: 197px;
    top: 30px;
    width: 806px;
    height: 1140px;
    display: block;
  }
  .poster-bg { fill: var(--poster-ink); }
  .frame-line { fill: none; stroke: var(--solar-blue); stroke-width: 2; }
  .hazard-stripe { fill: var(--solar-blue); }
  .headline {
    font-family: "Black Ops One", "Arial Black", sans-serif;
    text-anchor: middle;
  }
  .headline-blue { fill: var(--solar-blue); }
  .headline-white { fill: var(--chalk-white); }
  .glitch-line-white { stroke: var(--chalk-white); stroke-width: 3; }
  .glitch-line-blue { stroke: var(--solar-blue); stroke-width: 3; }
  .glitch-gap { fill: var(--poster-ink); }
  .brand-tab { fill: var(--solar-blue); }
  .brand-name {
    font-family: "Black Ops One", "Arial Black", sans-serif;
    fill: var(--poster-ink);
    text-anchor: middle;
    font-size: 30px;
  }
</style>
</head>
<body>
<svg class="poster" viewBox="0 0 677 958" xmlns="http://www.w3.org/2000/svg">
  <defs>
    <pattern id="stripes" width="14" height="14" patternUnits="userSpaceOnUse" patternTransform="rotate(30)">
      <rect class="hazard-stripe" width="6" height="14"/>
    </pattern>
    <pattern id="stripes-side" width="14" height="14" patternUnits="userSpaceOnUse" patternTransform="rotate(-60)">
      <rect class="hazard-stripe" width="6" height="14"/>
    </pattern>
  </defs>

  <rect class="poster-bg" width="677" height="958"/>

  <!-- frame -->
  <path class="frame-line" d="M330 31 H42 V275 L82 300 V600 L42 618 V923 H575 L635 862 V370 H598 V132 L635 100 V31"/>
  <rect x="327" y="31" width="308" height="22" fill="url(#stripes)"/>
  <rect x="42" y="618" width="40" height="305" fill="url(#stripes-side)"/>

  <!-- headline -->
  <text class="headline headline-blue" x="337" y="193" font-size="96" textLength="430" lengthAdjust="spacingAndGlyphs">PRACTICE</text>
  <text class="headline headline-white" x="350" y="310" font-size="98" textLength="425" lengthAdjust="spacingAndGlyphs">UNTIL YOU</text>
  <text class="headline headline-blue" x="343" y="486" font-size="160" textLength="420" lengthAdjust="spacingAndGlyphs">NEVER</text>
  <text class="headline headline-white" x="342" y="646" font-size="160" textLength="410" lengthAdjust="spacingAndGlyphs">GET IT</text>
  <text class="headline headline-blue" x="345" y="802" font-size="146" textLength="420" lengthAdjust="spacingAndGlyphs">WRONG</text>

  <!-- glitch slices -->
  <rect class="glitch-gap" x="120" y="160" width="440" height="2"/>
  <rect class="glitch-gap" x="135" y="430" width="420" height="2"/>
  <rect class="glitch-gap" x="130" y="600" width="440" height="2"/>
  <rect class="glitch-gap" x="130" y="735" width="440" height="2"/>
  <line class="glitch-line-white" x1="130" y1="282" x2="250" y2="282"/>
  <line class="glitch-line-white" x1="390" y1="258" x2="562" y2="258"/>
  <line class="glitch-line-blue" x1="113" y1="381" x2="552" y2="381"/>
  <line class="glitch-line-blue" x1="160" y1="458" x2="548" y2="458"/>
  <line class="glitch-line-white" x1="95" y1="590" x2="590" y2="590"/>
  <line class="glitch-line-white" x1="380" y1="490" x2="420" y2="490"/>
  <line class="glitch-line-blue" x1="110" y1="691" x2="540" y2="691"/>
  <line class="glitch-line-blue" x1="110" y1="773" x2="585" y2="773"/>

  <!-- brand tab -->
  <path class="brand-tab" d="M107 923 L118 884 H265 V828 H405 L417 840 V923 Z"/>
  <text class="brand-name" x="338" y="884" textLength="122" lengthAdjust="spacingAndGlyphs">VEXORIN</text>
</svg>
</body>
</html>
```